food label design

we need a label design for honey, we are beekeepers in WA/ Western Australia we produce many type of honey, so the label should suit all types. either by changing the name or colour variation etc, There is many great designs we have seen on google. But the design we had was not satisfying, maybe because we have seen many good ones that the design didn't impress us. We would like something that can be called premium and also unique
Updates

Target Market(s)

food, honey

Logo Text

amber wren

Font styles to use
Serif
Sans Serif
Decorative
Script

Colors

Designer to choose colors to be used in the design.

Requirements
Nice to have
• since the package already includes the logo design, could you guys just add the new logo design into the label? since that would make my selection of the winning project easier.
• the original logo, it did look nice but im not sure if its ok to have amber premium wren in the logo so yea. looking forward to see some new and better designs.
• Also it would be nice if designers can include the sizes of the label, or just some suggestion that could make it look better. since the size will affect like the word font etc bottle have different sizes.
• Also if can show the design on a honey bottle will be nice, we currently use hexagon bottle would consider cylinder in the future so if the design can include these would be perfect.
Should not have
• the attachment i included is the label design i have at the moment, it is nice but im not very impressed with it. Since one of the beekeepers in my State use almost the same design just different colour

```html
<!DOCTYPE html>
<html lang="en">
<head>
<meta charset="utf-8">
<title>Amber Wren – Honey Label</title>
<link rel="stylesheet" href="https://fonts.googleapis.com/css2?family=Cinzel:wght@500&family=Oswald:wght@300;400;600&display=swap">
<style>
  :root {
    --backdrop: #ececec;
    --label-peach: #f3cfa6;
    --ink: #1b1a18;
    --bronze: #6b4a1e;
    --cream: #f6e3c8;
    --gold-light: #e9d59a;
    --gold-dark: #a88a3e;
    --white: #ffffff;
  }
  * { box-sizing: border-box; margin: 0; padding: 0; }
  html, body { width: 1200px; height: 1037px; overflow: hidden; }
  body { background: var(--backdrop); position: relative; font-family: "Oswald", sans-serif; color: var(--ink); }

  /* Wrap-around jar label, flat */
  .wrap-label {
    position: absolute; left: 60px; top: 90px; width: 1080px; height: 400px;
    background: var(--label-peach); border-top: 16px solid var(--ink);
    display: grid; grid-template-columns: 360px 360px 360px;
  }
  .panel { position: relative; padding: 34px 30px; }
  .panel + .panel { border-left: 1px dashed rgba(27,26,24,0.18); }

  .panel--story p { font-size: 15px; line-height: 1.6; font-weight: 300; margin-bottom: 18px; }

  .panel--front { text-align: center; padding-top: 30px; }
  .brand-dot { width: 58px; height: 58px; border-radius: 50%; background: var(--ink); margin: 0 auto 14px; }
  .brand-name { font-family: "Cinzel", serif; font-weight: 500; font-size: 40px; letter-spacing: 1px; color: var(--ink); }
  .variety-box {
    margin: 24px -10px 0; background: var(--ink); display: flex; align-items: center;
    gap: 22px; padding: 16px 20px; text-align: left;
  }
  .variety-name { font-weight: 600; font-size: 34px; line-height: 1; color: var(--white); text-transform: uppercase; }
  .variety-origin { font-weight: 300; font-size: 19px; line-height: 1.15; color: var(--cream); text-transform: uppercase; }
  .net-weight { position: absolute; right: 22px; bottom: 22px; font-size: 16px; letter-spacing: 0.5px; text-transform: uppercase; }

  .warning { font-size: 14px; font-weight: 600; text-transform: uppercase; margin-bottom: 14px; }
  .nutrition { width: 100%; border-collapse: collapse; font-size: 14px; font-weight: 300; }
  .nutrition th, .nutrition td { border: 1px solid var(--ink); padding: 5px 8px; text-align: left; }
  .nutrition th { font-weight: 600; }
  .nutrition td:last-child { text-align: right; }

  /* Lid sticker */
  .lid-sticker {
    position: absolute; left: 350px; top: 560px; width: 400px; height: 400px; border-radius: 50%;
    background: var(--ink); border: 14px solid var(--gold-dark);
    box-shadow: inset 0 0 0 4px var(--gold-light);
    display: flex; flex-direction: column; align-items: center; justify-content: center; text-align: center;
  }
  .lid-sticker .brand-dot { width: 50px; height: 50px; background: var(--gold-light); margin-bottom: 18px; }
  .lid-sticker .brand-name { color: var(--white); font-size: 36px; }
  .lid-weight { margin-top: 22px; color: var(--white); font-size: 18px; text-transform: uppercase; letter-spacing: 0.5px; }

  /* Tamper seal strip */
  .seal-strip {
    position: absolute; left: 830px; top: 580px; width: 56px; height: 360px; background: var(--ink);
    display: flex; align-items: center; justify-content: center;
  }
  .seal-strip span {
    writing-mode: vertical-rl; transform: rotate(180deg); color: var(--white);
    font-size: 16px; letter-spacing: 1px; text-transform: uppercase; white-space: nowrap;
  }
</style>
</head>
<body>
  <section class="wrap-label">
    <div class="panel panel--story">
      <p>Pure raw honey to enjoy by the spoon.</p>
      <p>Gently extracted from local hives and then jarred by hand.</p>
      <p>Keep below 25°C</p>
    </div>

    <div class="panel panel--front">
      <div class="brand-dot"></div>
      <div class="brand-name">AMBER WREN</div>
      <div class="variety-box">
        <div class="variety-name">Clover<br>Flavour</div>
        <div class="variety-origin">Raw Western<br>Australian<br>Honey</div>
      </div>
      <div class="net-weight">Net Weight 250g</div>
    </div>

    <div class="panel panel--facts">
      <div class="warning">Do not feed to infants under 12 months</div>
      <table class="nutrition">
        <tr><th>Nutrition Information</th><th>Per 100g</th></tr>
        <tr><td>Energy</td><td>1340kJ</td></tr>
        <tr><td>Protein</td><td>0.4g</td></tr>
        <tr><td>Fat</td><td>0g</td></tr>
        <tr><td>Carbs</td><td>82g</td></tr>
        <tr><td>Sugars</td><td>80g</td></tr>
        <tr><td>Sodium</td><td>5mg</td></tr>
      </table>
    </div>
  </section>

  <div class="lid-sticker">
    <div class="brand-dot"></div>
    <div class="brand-name">AMBER WREN</div>
    <div class="lid-weight">Net Weight 250g</div>
  </div>

  <div class="seal-strip"><span>100% Natural Australian Honey</span></div>
</body>
</html>
```